New website design for tech company

I want to redesign the current website - https://lumarekin.co/
I want it to keep the same colors/branding but I want it to resemble the look and feel of the following sites
https://www.qorvanusa.com/
https://www.pradix.com/
https://www.jumplow.com/global/us/home
https://www.kettonplc.co.uk/

The site layout

Target Market(s)

tech companies

Industry/Entity Type

tech

Number of Pages Required

2 page

Font styles to use
Serif

Colors

Designer to choose colors to be used in the design.

Requirements
Must have
• a nice updated design that looks cutting edge and innovative and the site colors can match the current logo

```html
<!DOCTYPE html>
<html lang="en">
<head>
<meta charset="utf-8">
<title>Lumarekin — Home and Services</title>
<link rel="stylesheet" href="https://fonts.googleapis.com/css2?family=Playfair+Display:wght@400;500&family=Arimo:wght@400;700&display=swap">
<style>
:root{
  --stage:#2b2b2b;
  --ink:#000;
  --white:#fff;
  --soft:#d7dde6;
  --green:#6cc51d;
  --green-dark:#3f8a0e;
  --blue:#0d4fb2;
  --navy:#061a3d;
  --deep:#020c1f;
  --teal:#1d5a78;
  --serif:"Playfair Display",Georgia,serif;
  --sans:Arimo,Arial,sans-serif;
}
*{box-sizing:border-box;margin:0;padding:0}
html,body{width:691px;height:1200px;overflow:hidden}
body{background:var(--stage);position:relative;font-family:var(--sans);color:var(--white)}
.page{position:absolute;background:var(--ink);overflow:hidden}
.page--home{left:36px;top:26px;width:279px;height:1137px}
.page--services{left:352px;top:124px;width:299px;height:822px}
.abs{position:absolute}
.serif{font-family:var(--serif);font-weight:400}
.photo{position:absolute}

/* brand */
.brand{position:absolute;display:flex;align-items:center;gap:2px;font-family:var(--serif);color:var(--green);letter-spacing:.3px;text-transform:uppercase;font-weight:500}
.brand__dot{width:5px;height:5px;border-radius:50%;background:var(--green)}

/* nav */
.nav{position:absolute;display:flex;justify-content:space-between;font-family:var(--serif);font-size:3.6px;color:var(--white)}

/* buttons */
.btn{position:absolute;background:var(--green);color:var(--white);border-radius:6px;font-family:var(--serif);font-size:4px;display:flex;align-items:center;justify-content:center}

/* orb photos */
.orb{position:absolute;border-radius:50%;background:linear-gradient(120deg,#1446a6 0%,#0a2e6e 45%,#3e8f14 80%,#7bd227 100%);box-shadow:4px 0 10px rgba(108,197,29,.35)}
.orb .photo{border-radius:50%;inset:4px 7px 4px 4px}

.title{position:absolute;font-family:var(--serif);font-weight:400;color:var(--white);white-space:nowrap}
.title--rule::after{content:"";position:absolute;left:50%;bottom:-2px;width:44px;height:.6px;transform:translateX(-50%);background:linear-gradient(90deg,transparent,var(--green),transparent)}
.copy{position:absolute;font-size:4.3px;line-height:5.4px;color:var(--white)}

/* team */
.member{position:absolute;width:61px}
.member__photo{position:absolute;left:0;top:0;width:61px;height:53px;border:1px solid var(--green);background:linear-gradient(180deg,#8a8a8a,#3c3c3c)}
.member__name{position:absolute;top:56px;left:0;font-family:var(--serif);font-size:4.2px}
.member__role{position:absolute;top:63px;left:0;font-family:var(--serif);font-size:2.8px}

/* service cards */
.card{position:absolute;width:75px;height:79px;overflow:hidden}
.card__photo{position:absolute;left:0;top:0;width:75px;height:44px}
.card__panel{position:absolute;left:0;top:40px;width:75px;height:39px;background:linear-gradient(180deg,#6cc51d 0%,#4aa61b 45%,#1b63a8 100%);border-radius:50% 50% 0 0/6px 6px 0 0;text-align:center}
.card__icon{position:absolute;left:33px;top:-4px;width:9px;height:9px;border-radius:50%;background:#1a56b3;border:1px solid #bfe79b}
.card__name{position:absolute;top:8px;left:0;right:0;font-family:var(--serif);font-size:3.6px}
.card__text{position:absolute;top:15px;left:6px;right:6px;font-size:2.8px;line-height:3.4px}

/* lab */
.lab-card{position:absolute;height:63px;overflow:hidden}
.lab-card__name{position:absolute;left:7px;font-family:var(--serif);font-size:4.4px}
.lab-card__text{position:absolute;left:7px;right:10px;font-size:2.9px;line-height:3.4px}

/* partners */
.partner{position:absolute;top:750px;width:37px;height:25px;background:#3a3a3a;display:flex;align-items:center;justify-content:center}
.partner span{width:18px;height:6px;border-radius:3px;background:#8f8f8f}
.pager{position:absolute;width:6px;height:6px;border-radius:50%;background:#3a3a3a;border:.6px solid var(--green)}

/* contact */
.contact-item{position:absolute;display:flex;gap:4px;font-size:3px;line-height:3.6px}
.contact-item__icon{flex:none;width:5px;height:5px;border-radius:50%;background:var(--green);position:relative}
.social{position:absolute;display:flex;gap:4px}
.social span{width:4px;height:4px;border-radius:50%;background:var(--white)}
.field{position:absolute;border:.6px solid #c9d4e6;border-radius:2px;font-size:2.9px;padding:3px 4px;color:#e9eef6}
.badge{position:absolute;width:10px;height:10px;border-radius:50%;background:#d8f0c0;border:1.4px solid var(--green)}
.rule{position:absolute;height:.5px;background:#5d6677}
.copyright{position:absolute;left:0;right:0;text-align:center;font-size:3px}
</style>
</head>
<body>

<!-- HOME PAGE -->
<section class="page page--home" aria-label="Home page">
  <div class="photo" role="img" aria-label="Glowing blue particle wave on a dark background" style="left:0;top:0;width:279px;height:200px;background:radial-gradient(ellipse 140px 40px at 50% 70%,#2d7c9c 0%,#0e3650 45%,transparent 75%),linear-gradient(180deg,#000 0%,#04121f 35%,#0a2a3c 65%,#000 100%)"></div>

  <div class="brand" style="left:24px;top:7px;font-size:6px">Lumarekin<span class="brand__dot"></span></div>
  <nav class="nav" style="left:129px;top:8px;width:127px"><span>Home</span><span>About Us</span><span>Services</span><span>The Lab</span><span>Partner</span><span>Contact Us</span></nav>

  <svg class="abs" style="left:132px;top:41px" width="10" height="10" viewBox="0 0 10 10" aria-hidden="true"><circle cx="5" cy="5" r="4.3" fill="none" stroke="#fff" stroke-width=".8"/><path d="M4 3v4l3-2z" fill="#fff"/></svg>
  <p class="abs serif" style="left:0;right:0;top:58px;text-align:center;font-size:4.4px">Lumarekin - A subsidiary of Orrel &amp; Co.</p>
  <h1 class="abs serif" style="left:40px;right:40px;top:67px;text-align:center;font-size:13px;line-height:14.2px">Our vision is to provide ubiquitous ADA compliant web technologies to shift</h1>
  <div class="abs" style="left:94px;top:121px;width:24px;height:.5px;background:#fff"></div>
  <p class="abs serif" style="left:0;right:0;top:118px;text-align:center;font-size:4.4px">Humanity Forward</p>
  <div class="abs" style="left:161px;top:121px;width:24px;height:.5px;background:#fff"></div>
  <div class="btn" style="left:118px;top:130px;width:44px;height:11px">Ask Us How</div>

  <div class="orb" style="left:30px;top:174px;width:92px;height:88px"><div class="photo" role="img" aria-label="Professional woman surrounded by floating video call screens" style="background:linear-gradient(135deg,#dfe6ee,#9fb3c8 50%,#4a5d78)"></div></div>
  <h2 class="title" style="left:142px;top:183px;font-size:8px">What is Lumarekin?</h2>
  <p class="copy" style="left:142px;top:197px;width:106px">Lumarekin is a web based Internet and technology agency aimed at serving, educating, and partnering with brands &amp; organizations on how their products and services can advance the disabled community through inclusion and diversity. By integrating strategies, solutions, and practices accommodating all persons, we strive to shift humanity forward with the power of technology.</p>

  <div class="photo" role="img" aria-label="Night street scene with a runner passing through a glowing portal ring" style="left:0;top:268px;width:279px;height:119px;background:radial-gradient(circle at 78% 50%,#1b6d86 0%,#0a2d3e 30%,transparent 55%),linear-gradient(180deg,#000 0%,#0b1d28 40%,#13293a 80%,#000 100%)"></div>
  <h2 class="title" style="left:0;right:0;top:314px;text-align:center;font-size:8px">Mission Statement</h2>
  <p class="copy" style="left:60px;right:60px;top:329px;text-align:center;width:auto">To increase awareness and opportunities in the personal &amp; professional lives of disabled persons through technology, regardless of gender, age race or socio-economic background.</p>

  <div class="abs" style="left:0;top:387px;width:279px;height:120px;background:linear-gradient(180deg,#000 0%,#000 25%,#4a9b18 50%,#1f6e5a 75%,#0b4fb4 100%)"></div>
  <h2 class="title title--rule" style="left:0;right:0;top:406px;text-align:center;font-size:8px">The Team</h2>
  <div class="member" style="left:40px;top:431px"><div class="member__photo" role="img" aria-label="Portrait of the chief executive"></div><p class="member__name">Nadia Ferrow</p><p class="member__role">CEO</p></div>
  <div class="member" style="left:108px;top:431px"><div class="member__photo" style="background:#2b2f36"><p style="position:absolute;left:5px;right:5px;top:17px;text-align:center;font-size:2.8px;line-height:3.4px">Lorem ipsum dolor sit amet consectetur. Porttitor mauris nulla egestas.</p></div><p class="member__name" style="top:58px">Sam Porter</p><p class="member__role" style="top:65px">COO</p></div>
  <div class="member" style="left:178px;top:431px"><div class="member__photo" role="img" aria-label="Portrait of the chief operating lead"></div><p class="member__name" style="top:58px">Elliot Marsh</p><p class="member__role" style="top:65px">CO</p></div>

  <h2 class="title title--rule" style="left:0;right:0;top:518px;text-align:center;font-size:8px">Our Services</h2>
  <article class="card" style="left:24px;top:539px"><div class="card__photo" role="img" aria-label="Hands on a tablet with floating web code icons" style="background:linear-gradient(135deg,#1c2a44,#3b6fa8 60%,#0d1626)"></div><div class="card__panel"><span class="card__icon"></span><p class="card__name">Web &amp; Digital Accessibility</p><p class="card__text">Lorem ipsum dolor sit amet consectetur. Porttitor mauris nulla egestas.</p></div></article>
  <article class="card" style="left:103px;top:539px"><div class="card__photo" role="img" aria-label="Laptop screen filled with colourful code" style="background:linear-gradient(135deg,#0f1c2c,#2e6a88 55%,#1a2430)"></div><div class="card__panel"><span class="card__icon"></span><p class="card__name">Software Development</p><p class="card__text">Lorem ipsum dolor sit amet consectetur. Porttitor mauris nulla egestas.</p></div></article>
  <article class="card" style="left:182px;top:539px"><div class="card__photo" role="img" aria-label="Classroom with a presenter at a whiteboard" style="background:linear-gradient(135deg,#e8e2d8,#b79c7a 55%,#5c4a3a)"></div><div class="card__panel"><span class="card__icon"></span><p class="card__name">Training &amp; Education</p><p class="card__text">Lorem ipsum dolor sit amet consectetur. Porttitor mauris nulla egestas.</p></div></article>

  <div class="abs" style="left:0;top:631px;width:279px;height:86px;background:linear-gradient(180deg,#79d21f 0%,#4c9e14 45%,#1c3d06 80%,#000 100%)"></div>
  <h2 class="title" style="left:32px;top:668px;font-size:8px">The Lab</h2>
  <article class="lab-card" style="left:75px;top:645px;width:80px"><div class="photo" role="img" aria-label="Hands reviewing documents at a desk" style="inset:0;background:linear-gradient(180deg,#d8d4ce 0%,#7a736b 55%,#1e1b18 100%)"></div><p class="lab-card__name" style="top:35px">Lumen V.1</p><p class="lab-card__text" style="top:43px">Lorem ipsum dolor sit amet consectetur. Porttitor mauris nulla egestas.</p></article>
  <article class="lab-card" style="left:159px;top:645px;width:96px"><div class="photo" role="img" aria-label="Close-up of an eye within a digital network" style="inset:0;background:radial-gradient(circle at 60% 45%,#3aa3c4 0%,#124a6a 35%,#06142a 75%)"></div><p class="lab-card__name" style="top:37px">Lumarekin U</p><p class="lab-card__text" style="top:45px">Lorem ipsum dolor sit amet consectetur. Porttitor mauris nulla egestas.</p></article>

  <h2 class="title title--rule" style="left:0;right:0;top:728px;text-align:center;font-size:8px">Our Partners</h2>
  <span class="pager" style="left:25px;top:760px"></span>
  <div class="partner" style="left:43px"><span></span></div>
  <div class="partner" style="left:84px"><span></span></div>
  <div class="partner" style="left:125px"><span></span></div>
  <div class="partner" style="left:166px"><span></span></div>
  <div class="partner" style="left:207px"><span></span></div>
  <span class="pager" style="left:248px;top:759px"></span>
  <h2 class="title" style="left:0;right:0;top:783px;text-align:center;font-size:8px">Let’s Discuss How to Make your Business Better.</h2>
  <div class="btn" style="left:119px;top:801px;width:43px;height:11px">Get in Touch</div>

  <div class="photo" role="img" aria-label="Dark teal particle wave" style="left:0;top:840px;width:279px;height:125px;background:radial-gradient(ellipse 150px 30px at 40% 60%,#1f5f6e 0%,#0a2430 50%,transparent 80%),#000"></div>
  <h2 class="title" style="left:26px;top:854px;font-size:8px">WHy Choose Us</h2>
  <p class="copy" style="left:26px;top:872px;width:100px">Who does Lumarekin serve? A person regardless of legal or medical mandates with a physical and/or mental ailment that prevents them from using technology without the use of an assistive software.</p>
  <div class="orb" style="left:160px;top:843px;width:92px;height:88px"><div class="photo" role="img" aria-label="Handshake over a glowing circuit board" style="background:radial-gradient(circle at 50% 50%,#f0a24a 0%,#2a5aa8 30%,#0b2a66 80%)"></div></div>

  <div class="abs" style="left:0;top:952px;width:279px;height:140px;background:linear-gradient(180deg,#0d4aa8 0%,#082f6e 45%,#041634 80%,#000 100%);border-radius:50% 50% 0 0/8px 8px 0 0"></div>
  <h2 class="title" style="left:34px;top:976px;font-size:7.5px">Contact Us</h2>
  <div class="contact-item" style="left:37px;top:992px"><span class="contact-item__icon"></span>888-555-0142 (Toll-Free)</div>
  <div class="contact-item" style="left:37px;top:1000px"><span class="contact-item__icon"></span>hello@lumarekin.co</div>
  <div class="contact-item" style="left:37px;top:1008px"><span class="contact-item__icon"></span><span>Lumarekin<br>410 Alder Crest Way Ste 2<br>Brookhaven, MD 20899-0101<br>United States of America</span></div>
  <div class="social" style="left:37px;top:1038px"><span></span><span></span><span></span></div>
  <h2 class="title" style="left:140px;top:973px;font-size:7.5px">Request a Call Back Today Now!</h2>
  <div class="field" style="left:140px;top:992px;width:55px;height:11px">First name</div>
  <div class="field" style="left:198px;top:992px;width:56px;height:11px">Last name</div>
  <div class="field" style="left:140px;top:1006px;width:55px;height:11px">Email</div>
  <div class="field" style="left:198px;top:1006px;width:56px;height:11px">Phone Number</div>
  <div class="field" style="left:140px;top:1020px;width:114px;height:22px">Message</div>
  <div class="btn" style="left:140px;top:1048px;width:43px;height:11px">Send</div>

  <div class="brand" style="left:29px;top:1077px;font-size:9px">Lumarekin<span class="brand__dot" style="width:7px;height:7px"></span></div>
  <span class="badge" style="left:215px;top:1079px"></span>
  <span class="badge" style="left:228px;top:1079px"></span>
  <span class="badge" style="left:241px;top:1079px"></span>
  <div class="rule" style="left:29px;width:232px;top:1121px"></div>
  <p class="copyright" style="top:1126px">Copyright © 2023 Lumarekin - All Rights Reserved</p>
</section>

<!-- SERVICES PAGE -->
<section class="page page--services" aria-label="Services page">
  <div class="photo" role="img" aria-label="Digital wireframe hand reaching toward a human hand in blue space" style="left:0;top:0;width:299px;height:160px;background:radial-gradient(ellipse 110px 60px at 30% 65%,#2a6c8c 0%,transparent 70%),linear-gradient(180deg,#0d3a57 0%,#0a2c47 45%,#05121f 85%,#000 100%)"></div>
  <div class="brand" style="left:26px;top:8px;font-size:6px">Lumarekin<span class="brand__dot"></span></div>
  <nav class="nav" style="left:139px;top:9px;width:135px"><span>Home</span><span>About Us</span><span>Services</span><span>The Lab</span><span>Partner</span><span>Contact Us</span></nav>
  <h1 class="title" style="left:0;right:0;top:48px;text-align:center;font-size:14px">Our Services</h1>
  <p class="copy" style="left:66px;right:66px;top:68px;text-align:center;font-size:4.8px;line-height:6px">Lumarekin is a web based Internet and technology agency aimed at serving, educating, and partnering with brands &amp; organizations on how their products and services can advance the disabled community through inclusion and diversity. By integrating strategies, solutions, and practices accommodating all persons, we strive to shift humanity forward with the power of technology.</p>

  <div class="orb" style="left:32px;top:160px;width:100px;height:94px"><div class="photo" role="img" aria-label="Hands on a tablet with floating HTML icons" style="background:linear-gradient(135deg,#1a2940,#3a78b0 55%,#0b1424)"></div></div>
  <h2 class="title" style="left:163px;top:166px;font-size:8.5px;line-height:11px;white-space:normal;width:110px">Web &amp; Digital Accessibility Services</h2>
  <p class="copy" style="left:163px;top:194px;width:107px;font-size:4.1px;line-height:5px">Tailored to ensure seamless ADA compliant digital experiences for everyone. Specializes in enhancing website and app accessibility, adhering to WCAG guidelines. Offers comprehensive audits, user-friendly design consultations, and ongoing support to make digital content universally accessible. Ideal for organizations committed to inclusivity, improving user experience, and ensuring legal compliance.</p>

  <h2 class="title" style="left:38px;top:294px;font-size:8.5px">Software Development</h2>
  <p class="copy" style="left:37px;top:309px;width:112px;font-size:4.1px;line-height:5px">Lorem ipsum dolor sit amet consectetur. Rhoncus massa bibendum vulputate nec tellus amet tristique dictum vitae. Imperdiet quis ullamcorper nisi ultricies lacinia consectetur urna. Enim tincidunt arcu cursus eget cursus. Faucibus viverra vel cursus commodo molestie semper fermentum. Lacus diam tortor viverra eu lorem. Egestas maecenas mauris accumsan nibh. Sem commodo et malesuada id cursus tempus at. Eget gravida vitae nec tortor phasellus eleifend consectetur adipiscing.<br><br>Donec et ultricies eu amet. Ultrices non egestas quam diam. Sed vel ut egestas cursus mauris. Sem imperdiet ipsum semper massa sociis dui tincidunt facilisis odio.</p>
  <div class="orb" style="left:166px;top:287px;width:100px;height:94px"><div class="photo" role="img" aria-label="Person typing on a laptop showing colourful code" style="background:linear-gradient(135deg,#0f1c2c,#2e7090 55%,#141c28)"></div></div>

  <div class="orb" style="left:32px;top:414px;width:100px;height:94px"><div class="photo" role="img" aria-label="Classroom with a presenter at a whiteboard" style="background:linear-gradient(135deg,#efe9df,#b99e7c 55%,#4e3f33)"></div></div>
  <h2 class="title" style="left:163px;top:430px;font-size:8.5px">Training &amp; Education</h2>
  <p class="copy" style="left:163px;top:449px;width:107px;font-size:4.1px;line-height:5px">Tailored to ensure seamless ADA compliant digital experiences for everyone. Specializes in enhancing website and app accessibility, adhering to WCAG guidelines. Offers comprehensive audits, user-friendly design consultations, and ongoing support to make digital content universally accessible. Ideal for organizations committed to inclusivity, improving user experience, and ensuring legal compliance.</p>

  <div class="photo" role="img" aria-label="Tunnel of glowing blue data panels" style="left:0;top:500px;width:299px;height:125px;background:radial-gradient(ellipse 90px 50px at 50% 55%,#2c6d96 0%,#143b5c 45%,transparent 80%),linear-gradient(180deg,#000 0%,#0d2a44 35%,#123a5c 70%,#0a2c66 100%)"></div>
  <p class="copy" style="left:74px;right:74px;top:557px;text-align:center;font-size:4.8px;line-height:6px">Ensuring that your web based platform is partnered with Lumarekin will provide the peace of mind that you are offering all WCAG standards and offering the members of the disabled community the equal opportunity to apply, obtain, and successful maintain and flourish within your company.</p>

  <div class="abs" style="left:0;top:624px;width:299px;height:130px;background:linear-gradient(180deg,#0b3f95 0%,#082e6c 45%,#04173a 80%,#000 100%)"></div>
  <h2 class="title" style="left:31px;top:649px;font-size:7.5px">Contact Us</h2>
  <div class="contact-item" style="left:34px;top:666px"><span class="contact-item__icon"></span>888-555-0142 (Toll-Free)</div>
  <div class="contact-item" style="left:34px;top:674px"><span class="contact-item__icon"></span>hello@lumarekin.co</div>
  <div class="contact-item" style="left:34px;top:682px"><span class="contact-item__icon"></span><span>Lumarekin<br>410 Alder Crest Way Ste 2<br>Brookhaven, MD 20899-0101<br>United States of America</span></div>
  <div class="social" style="left:35px;top:706px"><span></span><span></span><span></span></div>
  <h2 class="title" style="left:144px;top:646px;font-size:7.5px">Request a Call Back Today Now!</h2>
  <div class="field" style="left:144px;top:665px;width:59px;height:12px">First name</div>
  <div class="field" style="left:206px;top:665px;width:59px;height:12px">Last name</div>
  <div class="field" style="left:144px;top:680px;width:59px;height:12px">Email</div>
  <div class="field" style="left:206px;top:680px;width:59px;height:12px">Phone Number</div>
  <div class="field" style="left:144px;top:696px;width:121px;height:23px">Message</div>
  <div class="btn" style="left:144px;top:726px;width:46px;height:12px">Send</div>

  <div class="brand" style="left:25px;top:758px;font-size:9px">Lumarekin<span class="brand__dot" style="width:7px;height:7px"></span></div>
  <p class="copy" style="left:27px;top:774px;width:80px;font-size:3px;line-height:3.8px">Lorem ipsum dolor sit amet consectetur. In sit viverra aliquam elit adipiscing maecenas. Congue morbi nam mi tristique aliquet congue.</p>
  <div class="contact-item" style="left:125px;top:762px"><span class="contact-item__icon"></span>888-555-0142 (Toll-Free)</div>
  <div class="contact-item" style="left:125px;top:770px"><span class="contact-item__icon"></span>hello@lumarekin.co</div>
  <div class="contact-item" style="left:125px;top:778px"><span class="contact-item__icon"></span><span>Lumarekin<br>410 Alder Crest Way Ste 2<br>Brookhaven, MD 20899-0101<br>United States of America</span></div>
  <span class="badge" style="left:226px;top:760px"></span>
  <span class="badge" style="left:239px;top:760px"></span>
  <span class="badge" style="left:253px;top:760px"></span>
  <div class="rule" style="left:25px;width:248px;top:805px"></div>
  <p class="copyright" style="top:811px">Copyright © 2023 Lumarekin - All Rights Reserved</p>
</section>

</body>
</html>
```